Modern 6 page design, business card, and a banner

I need a website design for my CFO service. The service uses proprietary tech, so it needs to be modern. I also need business card and banner design to match the site.
The banner size is 33.75 X 79.25.
I'm open to colors and styles.

Target Market(s)

Startups

Coding

Coded - Design and coding required

Number of Pages Required

5+ page

```html
<!DOCTYPE html>
<html lang="en">
<head>
<meta charset="utf-8">
<title>Vantr – Strategic Financial Planner</title>
<link href="https://fonts.googleapis.com/css2?family=Lato:wght@300;400;700&display=swap" rel="stylesheet">
<style>
:root{
  --blue:#2a5cab;
  --navy:#1f4f9c;
  --ink:#333;
  --text:#444;
  --pale:#eef3fb;
  --dark:#1b1b1b;
  --olive:#9a9a5f;
  --orange:#c1592c;
  --teal:#347a7b;
  --pink:#e8395b;
  --green:#7b9a58;
  --white:#fff;
}
*{box-sizing:border-box;margin:0;padding:0}
html,body{width:1200px;height:3142px;overflow:hidden}
body{font-family:'Lato',sans-serif;color:var(--text);background:var(--white);position:relative}
section,header,footer{position:absolute;left:0;width:1200px}
.btn{display:inline-block;border-radius:26px;font-weight:700;font-size:18px;text-align:center;line-height:50px;height:50px;width:194px;text-decoration:none}
.btn-blue{background:var(--blue);color:var(--white)}
.btn-white{background:var(--white);color:var(--blue);width:178px;height:48px;line-height:48px}
.btn-dark{background:#151515;color:var(--white);width:178px;height:48px;line-height:48px}

/* hero */
.hero{top:0;height:661px;background:linear-gradient(135deg,#3b3530 0%,#6e6a66 35%,#bdb8b1 60%,#8c857c 100%);overflow:hidden}
.hero-photo{position:absolute;inset:0;background:radial-gradient(ellipse at 70% 45%,rgba(235,235,240,.55),rgba(0,0,0,0) 55%),linear-gradient(180deg,rgba(0,0,0,.15),rgba(0,0,0,.35))}
.brand{position:absolute;left:75px;top:22px;color:var(--white)}
.brand-name{font-weight:300;font-size:58px;letter-spacing:1px;line-height:64px}
.brand-tag{font-size:17px;margin-top:2px}
.nav{position:absolute;top:55px;left:462px;display:flex;gap:0}
.nav a{color:var(--white);font-weight:700;font-size:16px;text-decoration:none;height:44px;line-height:44px;padding:0 18px}
.nav a.active{background:var(--blue);border-radius:22px;padding:0 28px}
.hero h1{position:absolute;top:278px;left:0;width:1200px;text-align:center;color:var(--white);font-weight:700;font-size:36px;line-height:44px;text-shadow:0 1px 3px rgba(0,0,0,.3)}
.dots{position:absolute;top:587px;left:568px;display:flex;gap:9px}
.dots span{width:10px;height:10px;border-radius:50%;background:var(--white)}
.dots span.on{background:var(--blue)}

/* welcome */
.welcome{top:661px;height:421px;text-align:center}
.welcome h2{margin-top:50px;font-weight:400;font-size:46px;color:var(--ink)}
.welcome p{font-size:16px;line-height:28px;width:1030px;margin:0 auto}
.welcome p.first{margin-top:16px}
.welcome p+p{margin-top:9px}
.welcome .btn{margin-top:38px}

/* how */
.how{top:1082px;height:578px;background:var(--pale)}
.how h2{text-align:center;margin-top:44px;font-weight:400;font-size:46px;color:var(--ink)}
.steps{position:absolute;left:75px;top:140px;display:flex;gap:10px}
.step{width:203px;position:relative;height:380px}
.step svg.arrow{position:absolute;left:0;top:52px}
.step .icon{position:absolute;left:59px;top:2px;width:84px;height:84px;border-radius:50%;background:var(--white);box-shadow:0 4px 8px rgba(0,0,0,.3);display:flex;align-items:center;justify-content:center}
.step .stem{position:absolute;left:95px;top:110px;width:14px;height:50px}
.step .card{position:absolute;left:0;top:158px;width:203px;color:var(--white);text-align:center;padding:22px 14px 0}
.card h3{font-size:19px;font-weight:700;margin-bottom:6px}
.card p{font-size:14.5px;line-height:23px}
.s1{--c:var(--olive)}.s2{--c:var(--orange)}.s3{--c:var(--teal)}.s4{--c:var(--pink)}.s5{--c:var(--green)}
.step .stem,.step .card{background:var(--c)}

/* app */
.app{top:1660px;height:615px}
.app h2{position:absolute;left:134px;top:112px;font-weight:400;font-size:46px;color:var(--ink)}
.app .copy{position:absolute;left:135px;top:186px;width:600px;font-size:16px;line-height:28px}
.app .lead{color:var(--blue);font-weight:700}
.app .strong{color:#111;font-weight:700;margin-top:14px}
.app .btn{position:absolute;left:136px;top:438px}
.phone{position:absolute;left:832px;top:70px;width:230px;height:475px;border-radius:34px;background:linear-gradient(180deg,#f3f4f6,#d9dce0);border:3px solid #c5c9ce}
.phone-screen{position:absolute;left:9px;top:50px;width:206px;height:355px;background:linear-gradient(180deg,#1e2a5a,#162466)}

/* why */
.why{top:2275px;height:390px;background:var(--pale)}
.why-photo{position:absolute;left:0;top:0;width:482px;height:390px;background:linear-gradient(120deg,#5c6e86,#b8c4d0 45%,#7d8a99)}
.why h2{position:absolute;left:523px;top:70px;font-weight:400;font-size:46px;color:var(--ink)}
.why p{position:absolute;left:524px;top:144px;width:600px;font-size:16px;line-height:28px}

/* about/contact */
.info{top:2665px;height:417px;background:var(--navy);color:var(--white)}
.info h2{font-weight:400;font-size:46px;line-height:56px}
.about{position:absolute;left:75px;top:58px;width:420px}
.about p{font-size:16px;font-weight:400;line-height:28px;margin-top:16px}
.about .btn{margin-top:34px}
.contact{position:absolute;left:524px;top:58px;width:602px;height:330px}
.form{margin-top:20px;display:grid;grid-template-columns:293px 293px;gap:10px 15px}
.field{background:var(--white);color:#333;border-radius:22px;height:44px;line-height:44px;padding:0 22px;font-size:13.5px}
.field.msg{grid-column:1/3;height:76px;border-radius:12px;line-height:20px;padding-top:12px}
.contact .btn{position:absolute;right:0;top:273px}

/* footer */
.footer{top:3082px;height:60px;background:var(--dark)}
.footer small{position:absolute;left:75px;top:24px;font-size:12px;color:#8a8a8a}
.social{position:absolute;right:82px;top:20px;display:flex;gap:22px}
.social span{width:22px;height:22px;border-radius:50%;background:var(--white)}
</style>
</head>
<body>

<header class="hero">
  <div class="hero-photo" role="img" aria-label="Photo of a person checking a finance chart on a phone in front of a laptop showing a bar chart"></div>
  <div class="brand">
    <div class="brand-name">Vantr</div>
    <div class="brand-tag">Strategic Financial Planner</div>
  </div>
  <nav class="nav">
    <a class="active" href="#">Home</a>
    <a href="#">About Us</a>
    <a href="#">How It Works</a>
    <a href="#">Why Vantr</a>
    <a href="#">Vantr App</a>
    <a href="#">Contact Us</a>
  </nav>
  <h1>Vantr combines hands-on financial planning services<br>with real-time mobile monitoring.</h1>
  <div class="dots"><span class="on"></span><span></span><span></span><span></span></div>
</header>

<section class="welcome">
  <h2>Welcome to Vantr</h2>
  <p class="first">Small businesses can visualize their finances, have a plan they trust and monitor progress daily. No more waiting for the latest monthly or quarterly report from your accountant. No more late nights digging through spreadsheets to figure out where you really stand. No more wondering if you’re prepared for the future.</p>
  <p>Vantr delivers a clear financial plan tailored to your goals, an easy mobile dashboard to track progress on a daily basis and all the professional advice and support you need along the way.</p>
  <a class="btn btn-blue" href="#">Read More</a>
</section>

<section class="how">
  <h2>How It Works</h2>
  <div class="steps">
    <div class="step s1">
      <svg class="arrow" width="203" height="62" viewBox="0 0 203 62"><polygon points="0,0 175,0 203,31 175,62 0,62 28,31" fill="var(--c)"/></svg>
      <div class="stem"></div>
      <div class="icon"><svg width="26" height="30" viewBox="0 0 26 30"><path d="M2 1h15l7 7v21H2z" fill="var(--olive)"/><path d="M7 14h12M7 19h12M7 24h12" stroke="#fff" stroke-width="2"/></svg></div>
      <div class="card" style="height:192px"><h3>Develop Plan</h3><p>We work with you to develop a 3 to 5 year financial plan tailored to your business goals.</p></div>
    </div>
    <div class="step s2">
      <svg class="arrow" width="203" height="62" viewBox="0 0 203 62"><polygon points="0,0 175,0 203,31 175,62 0,62 28,31" fill="var(--c)"/></svg>
      <div class="stem"></div>
      <div class="icon"><svg width="36" height="30" viewBox="0 0 36 30"><circle cx="13" cy="17" r="8" fill="none" stroke="var(--orange)" stroke-width="6" stroke-dasharray="4 2.3"/><circle cx="27" cy="8" r="5" fill="none" stroke="var(--orange)" stroke-width="4" stroke-dasharray="3 1.8"/><circle cx="27" cy="24" r="4" fill="none" stroke="var(--orange)" stroke-width="3"/></svg></div>
      <div class="card" style="height:214px"><h3>Clean Data</h3><p>Our bookkeepers clean your historical data, set-up live data intake, and ensure alignment with finance reports.</p></div>
    </div>
    <div class="step s3">
      <svg class="arrow" width="203" height="62" viewBox="0 0 203 62"><polygon points="0,0 175,0 203,31 175,62 0,62 28,31" fill="var(--c)"/></svg>
      <div class="stem"></div>
      <div class="icon"><svg width="22" height="34" viewBox="0 0 22 34"><text x="11" y="29" text-anchor="middle" font-family="Lato,sans-serif" font-weight="700" font-size="34" fill="var(--teal)">$</text></svg></div>
      <div class="card" style="height:192px"><h3>Visual Finances</h3><p>We launch your customized visual finance dashboard on Vantr Mobile.</p></div>
    </div>
    <div class="step s4">
      <svg class="arrow" width="203" height="62" viewBox="0 0 203 62"><polygon points="0,0 175,0 203,31 175,62 0,62 28,31" fill="var(--c)"/></svg>
      <div class="stem"></div>
      <div class="icon"><svg width="34" height="28" viewBox="0 0 34 28"><path d="M2 2v24h30" fill="none" stroke="var(--pink)" stroke-width="3"/><rect x="8" y="14" width="4" height="10" fill="var(--pink)"/><rect x="14" y="8" width="4" height="16" fill="var(--pink)"/><rect x="20" y="12" width="4" height="12" fill="var(--pink)"/><rect x="26" y="5" width="4" height="19" fill="var(--pink)"/></svg></div>
      <div class="card" style="height:214px"><h3>Monitor Daily</h3><p>You monitor real financial results against plan on a daily basis.</p></div>
    </div>
    <div class="step s5">
      <svg class="arrow" width="203" height="62" viewBox="0 0 203 62"><polygon points="0,0 175,0 203,31 175,62 0,62 28,31" fill="var(--c)"/></svg>
      <div class="stem"></div>
      <div class="icon"><svg width="30" height="30" viewBox="0 0 30 30"><rect x="2" y="5" width="26" height="23" fill="none" stroke="var(--green)" stroke-width="3"/><rect x="2" y="5" width="26" height="6" fill="var(--green)"/><path d="M8 2v6M22 2v6M2 17h26M2 23h26M9 11v17M15 11v17M21 11v17" stroke="var(--green)" stroke-width="2"/></svg></div>
      <div class="card" style="height:192px"><h3>Advise Monthly</h3><p>Our financial experts provide support and help respond as your business grows.</p></div>
    </div>
  </div>
</section>

<section class="app">
  <h2>Vantr Mobile App</h2>
  <div class="copy">
    <p class="lead">Visualize your finances in real time.</p>
    <p>Vantr delivers an easy-to-understand dashboard using our own mobile app, customized for your business and your specific plan. Relying on clean data and mirroring your actual financial statements, Vantr lets you see what a CFO sees and always be confident you’re looking at real numbers.</p>
    <p class="strong">Monitor results daily, understand where you stand versus plan and make better decisions with Vantr Mobile.</p>
  </div>
  <a class="btn btn-blue" href="#">Learn More</a>
  <div class="phone">
    <div class="phone-screen" role="img" aria-label="Mobile dashboard showing income, expenses, cash and loan gauges"></div>
  </div>
</section>

<section class="why">
  <div class="why-photo" role="img" aria-label="Photo of a hand holding a smartphone with bar charts in an office lobby"></div>
  <h2>Why Vantr Visual Finance?</h2>
  <p>Small businesses shouldn’t be forced to choose between the strategic value of traditional financial services and the convenience of modern mobile reporting technology. With Vantr, you have access to decades of financial planning experience and a daily view into real finance reports - all delivered through a mobile app you can take with you on the road, in the field, on the shop floor or wherever you need to be.</p>
</section>

<section class="info">
  <div class="about">
    <h2>About Vantr</h2>
    <p>Lorem ipsum dolor sit amet, consectetur adipiscing elit. In tellus metus, mollis non lorem in, pretium tempor leo. Donec molestie turpis pellentesque facilisis interdum. Morbi vel nisl imperdiet, maximus magna vitae, eleifend orci. Integer egestas non nisl suscipit aliquam.</p>
    <a class="btn btn-white" href="#">Learn More</a>
  </div>
  <div class="contact">
    <h2>Contact Us</h2>
    <div class="form">
      <div class="field">Enter Name</div>
      <div class="field">Enter Email Address</div>
      <div class="field">Phone No</div>
      <div class="field">Subject</div>
      <div class="field msg">Message</div>
    </div>
    <a class="btn btn-dark" href="#">Submit</a>
  </div>
</section>

<footer class="footer">
  <small>Copyright © 2019 Company Name. All Rights Reserved.</small>
  <div class="social"><span></span><span></span><span></span><span></span><span></span></div>
</footer>

</body>
</html>
```